Promotional Poster for Brightwave a Charity Event in Hartford

This poster will be used for promotional purposes for an event called BrightWave.
BrightWave showcases the cultural resources and services Hartford, Connecticut has to offer. The event brings groups from around the area to promote what they can do for the residents of our city.
I've attached a file called "lame-mockup" of a quick and dirty mockup of what we thought would look great.
Since this event is strongly connected with Hartford I'd really like the post to emphasize the shape or outline of our city borders. We want a stylized sort of map and not a strait up clone of roamly charts.
We don't want a 1:1 clone of roamly charts but maybe something stylized to match the colors of the logo. Maybe the other elements float over the map? Maybe the map only had highways, parks and rivers. We do want to include some text or slogan.
The logo and the date should be featured on top and probably should include the year since we don't want people to think its a poster leftover from last year. There should be some space for a slogan like "Connecting Hartford Communities".
There is a logo file attached. Now the logo can be tweaked a little to better fit the design. Feel free to remove the chrome embossing or rearrange the loops and the text to make the logo more horizontal or vertical as you see fit. The three hoopy thing and the colors should stay the same though.
On the bottom of the poster we need to have a collection of our participating organizations. There is a zip file attached called "logos" which has all logos. Just try and fit them all best you can.
Thanks for your help.
!Updates!
The bullets in the "lame-mockup" file should be:
Local Musicians
Fresh Food
Art Walk
Children's Activities
Pop-Up Street Store
The event only goes until 6pm.

```html
<!DOCTYPE html>
<html lang="en">
<head>
<meta charset="utf-8">
<title>BrightWave — Connecting Hartford Communities</title>
<link rel="stylesheet" href="https://fonts.googleapis.com/css2?family=Oswald:wght@300;400;500;600&display=swap">
<style>
  :root {
    --sky-top: #4a5b69;
    --sky-mid: #8593a0;
    --sky-low: #d6dbde;
    --map-river: rgba(120, 190, 225, 0.45);
    --map-road: rgba(230, 140, 60, 0.28);
    --ink: #ffffff;
    --circle: #1d2a36;
    --circle-ring: #3b5061;
    --band: rgba(210, 222, 228, 0.14);
    --teal: #b9dbe6;
    --teal-strong: #e2f1f6;
    --brand: #d8395a;
    --badge-a: #4c8fc7;
    --badge-b: #e06b2a;
    --badge-c: #6aa84f;
    --badge-d: #8b5fa8;
    --badge-e: #d23b3b;
    --badge-f: #2d3e50;
    --badge-g: #e2a72e;
  }
  * { margin: 0; padding: 0; box-sizing: border-box; }
  html, body { width: 876px; height: 1200px; overflow: hidden; }
  body { font-family: "Oswald", sans-serif; background: var(--sky-low); }
  .poster { position: relative; width: 876px; height: 1200px; overflow: hidden; }
  .city-map {
    position: absolute; inset: 0;
    background:
      radial-gradient(ellipse 260px 700px at 760px 300px, var(--map-river), transparent 70%),
      radial-gradient(ellipse 420px 260px at 300px 180px, var(--map-road), transparent 70%),
      linear-gradient(180deg, var(--sky-top) 0%, var(--sky-mid) 45%, var(--sky-low) 80%, #e6e9eb 100%);
  }
  .event-date { position: absolute; left: 24px; top: 6px; color: var(--ink); }
  .event-date .day { font-size: 66px; font-weight: 500; letter-spacing: 1px; line-height: 1.1; }
  .event-date .hours { font-size: 34px; font-weight: 400; letter-spacing: 1px; line-height: 1.1; }
  .brand { position: absolute; right: 24px; top: 70px; display: flex; flex-direction: column; align-items: center; gap: 8px; }
  .brand-row { display: flex; align-items: center; gap: 10px; }
  .brand-dot { width: 46px; height: 46px; border-radius: 50%; background: var(--brand); }
  .brand-name { font-size: 36px; font-weight: 600; color: var(--brand); }
  .brand-sub { font-size: 15px; font-weight: 400; color: var(--ink); letter-spacing: 0.5px; }
  .hero { position: absolute; left: 181px; top: 231px; width: 514px; height: 514px; }
  .slogan { position: absolute; left: 0; right: 0; top: 425px; text-align: center; color: var(--teal); font-weight: inherit; }
  .slogan span { display: block; }
  .slogan .small { font-size: 56px; font-weight: 300; letter-spacing: 1px; line-height: 1.15; }
  .slogan .big { font-size: 104px; font-weight: 500; letter-spacing: 2px; line-height: 1; color: var(--teal-strong); }
  .features { position: absolute; left: 24px; top: 772px; color: var(--ink); text-transform: uppercase; }
  .features h2 { font-size: 32px; font-weight: 500; letter-spacing: 1px; line-height: 1.2; }
  .features li { list-style: none; font-size: 25px; font-weight: 400; line-height: 1.2; letter-spacing: 0.5px; }
  .partners { position: absolute; left: 14px; right: 14px; top: 1008px; display: flex; flex-direction: column; gap: 14px; }
  .partner-row { display: flex; gap: 14px; justify-content: space-between; }
  .partner-row.first { justify-content: flex-end; gap: 26px; }
  .partner { height: 50px; border-radius: 6px; }
  .partner.round { width: 54px; height: 54px; border-radius: 50%; }
  .partner.wide { width: 120px; }
  .partner.mid { width: 84px; }
</style>
</head>
<body>
<main class="poster">
  <div class="city-map" role="img" aria-label="Stylized map of Hartford with highways, parks and the river"></div>

  <header class="event-date">
    <div class="day">JUNE 13, 2015</div>
    <div class="hours">11 AM - 6 PM</div>
  </header>

  <div class="brand">
    <div class="brand-row"><span class="brand-dot"></span><span class="brand-name">BrightWave</span></div>
    <div class="brand-sub">Civic Arts Council</div>
  </div>

  <svg class="hero" viewBox="0 0 514 514" aria-hidden="true">
    <defs><clipPath id="disc"><circle cx="257" cy="257" r="250"/></clipPath></defs>
    <circle cx="257" cy="257" r="256" fill="var(--circle-ring)" opacity="0.55"/>
    <circle cx="257" cy="257" r="246" fill="var(--circle)"/>
    <rect x="0" y="195" width="514" height="150" fill="var(--band)" clip-path="url(#disc)"/>
  </svg>

  <h1 class="slogan">
    <span class="small">CONNECTING</span>
    <span class="big">HARTFORD</span>
    <span class="small">COMMUNITIES</span>
  </h1>

  <section class="features">
    <h2>Featuring</h2>
    <ul>
      <li>Local Musicians</li>
      <li>Fresh Food</li>
      <li>Artwalk</li>
      <li>Children's Activities</li>
      <li>Pop-Up Street Store</li>
    </ul>
  </section>

  <section class="partners" aria-label="Participating organizations">
    <div class="partner-row first">
      <span class="partner round" style="background:var(--badge-e)"></span>
      <span class="partner round" style="background:var(--badge-a)"></span>
      <span class="partner round" style="background:var(--badge-c)"></span>
      <span class="partner round" style="background:var(--badge-g)"></span>
      <span class="partner round" style="background:var(--badge-b)"></span>
      <span class="partner round" style="background:var(--badge-d)"></span>
    </div>
    <div class="partner-row">
      <span class="partner wide" style="background:var(--badge-a)"></span>
      <span class="partner mid" style="background:var(--badge-f)"></span>
      <span class="partner mid" style="background:var(--badge-c)"></span>
      <span class="partner mid" style="background:var(--badge-b)"></span>
      <span class="partner mid" style="background:var(--badge-e)"></span>
      <span class="partner mid" style="background:var(--badge-d)"></span>
      <span class="partner mid" style="background:var(--badge-g)"></span>
    </div>
    <div class="partner-row">
      <span class="partner wide" style="background:var(--badge-f)"></span>
      <span class="partner mid" style="background:var(--badge-b)"></span>
      <span class="partner wide" style="background:var(--badge-c)"></span>
      <span class="partner mid" style="background:var(--badge-a)"></span>
      <span class="partner mid" style="background:var(--badge-d)"></span>
      <span class="partner wide" style="background:var(--badge-e)"></span>
    </div>
  </section>
</main>
</body>
</html>
```